Buch-/E-Book-Cover für Sammlung von positiven Erfahrungen
Zielgruppe
die Zielgruppe sind Väter die ihren Söhne eine Sammlung von Empfehlungen für ein positives Leben schenken sollen. Der Titel des Buches heisst 'Zwischen Ebbe und Glut'
Aufgabenstellung
ich möchte mich hier von den Designern überraschen und inspirieren lassen.

```html
<!DOCTYPE html>
<html lang="de">
<head>
<meta charset="utf-8">
<title>Zwischen Ebbe und Glut – Buchcover</title>
<link href="https://fonts.googleapis.com/css2?family=Arimo:wght@400;500&display=swap" rel="stylesheet">
<style>
  :root {
    --sky-top: #eef1f4;
    --mist: #d3dde6;
    --lake: #b9cad8;
    --lake-deep: #a9bccb;
    --ink: #17171c;
    --rule: #2a2a30;
    --copper: #b27a42;
    --navy: #15152b;
    --paper: #ffffff;
  }
  html, body {
    margin: 0;
    padding: 0;
    width: 930px;
    height: 1200px;
    overflow: hidden;
    background: var(--paper);
  }
  .cover {
    position: relative;
    width: 930px;
    height: 1200px;
    overflow: hidden;
    font-family: "Arimo", Arial, sans-serif;
    color: var(--ink);
  }
  .cover-photo {
    position: absolute;
    inset: 0 0 185px 0;
    background:
      radial-gradient(ellipse at 30% 18%, rgba(120,110,100,0.35) 0%, rgba(120,110,100,0) 45%),
      linear-gradient(180deg, var(--sky-top) 0%, var(--mist) 28%, var(--lake) 52%, var(--lake-deep) 100%);
  }
  .title-block {
    position: absolute;
    left: 0;
    right: 0;
    top: 495px;
    text-align: center;
  }
  .title-small {
    display: flex;
    align-items: center;
    justify-content: center;
    gap: 22px;
    font-size: 32px;
    line-height: 1;
  }
  .title-small::before,
  .title-small::after {
    content: "";
    display: block;
    width: 250px;
    height: 2px;
    background: var(--rule);
  }
  .title-small.lead { margin-left: 10px; }
  .title-large {
    font-size: 122px;
    font-weight: 400;
    line-height: 1;
    letter-spacing: 2px;
    margin: 18px 0 22px;
  }
  .title-large.last { font-size: 140px; margin: 14px 0 0; }
  .title-rule {
    width: 730px;
    height: 2px;
    background: var(--rule);
    margin: 14px auto 0;
  }
  .subtitle {
    font-size: 26px;
    line-height: 1.15;
    letter-spacing: 0.5px;
    text-transform: uppercase;
    margin: 10px 0 0 -20px;
  }
  .copper-line {
    position: absolute;
    left: 0;
    right: 0;
    bottom: 185px;
    height: 6px;
    background: var(--copper);
  }
  .author-band {
    position: absolute;
    left: 0;
    right: 0;
    bottom: 0;
    height: 179px;
    background: var(--navy);
    display: flex;
    align-items: center;
    justify-content: center;
  }
  .author-name {
    color: var(--paper);
    font-size: 38px;
    letter-spacing: 5px;
    text-transform: uppercase;
    margin-top: -40px;
  }
</style>
</head>
<body>
<main class="cover">
  <div class="cover-photo" role="img" aria-label="Foto: Vater und Sohn sitzen barfuß auf einem hölzernen Steg über einem ruhigen Bergsee im Nebel"></div>

  <section class="title-block">
    <div class="title-small lead">Zwischen</div>
    <h1 class="title-large">EBBE</h1>
    <div class="title-small">und</div>
    <div class="title-large last">GLUT</div>
    <div class="title-rule"></div>
    <p class="subtitle">Eine Sammlung von Empfehlungen<br>für ein positives Leben</p>
  </section>

  <div class="copper-line"></div>
  <footer class="author-band">
    <span class="author-name">Lorenz Brückmann</span>
  </footer>
</main>
</body>
</html>
```